Website design for an Italian restaurant in Amsterdam

I need a design for a client of mine. It is for Teatro Lunaverde, an Italian restaurant in Amsterdam.
We are going for a clean, modern look but we also need to realise an authentic feel.
The restaurant is located in an old movie theatre, that is where the name Teatro Lunaverde comes from.
Industry/Entity Type
Italian Restaurant
Number of Pages Required
1 page
Font styles to use
Sans Serif
Colors
Designer to choose colors to be used in the design.

```html
<!DOCTYPE html>
<html lang="en">
<head>
<meta charset="utf-8">
<title>Teatro Lunaverde — Italian Cuisine</title>
<link rel="stylesheet" href="https://fonts.googleapis.com/css2?family=Open+Sans:wght@400;600;700&family=Playball&family=Playfair+Display:ital,wght@0,700;1,700&display=swap">
<style>
:root{
  --ink:#1b1b1b;
  --white:#ffffff;
  --nav:#141414;
  --hero-a:#3a2a26;
  --hero-b:#17121a;
  --welcome:#d6d6d6;
  --faint:#9a9a9a;
  --about:#2d4a30;
  --quote-bg:#ebebeb;
  --red:#e03c3e;
  --deep-red:#b01012;
  --chefs:#5b5b5b;
  --chef-green:#2b4a2d;
  --menu-a:#3d5a2c;
  --menu-b:#15171c;
  --contacts:#5f7a65;
  --field:#4f4f4f;
  --footer:#0d0d0d;
  --photo-warm:#8b6a55;
  --photo-dark:#4a3a34;
}
*{margin:0;padding:0;box-sizing:border-box}
html,body{width:1200px;height:4511px;overflow:hidden}
body{font-family:"Open Sans",Arial,sans-serif;color:var(--white);background:var(--white)}
section,header,footer{position:absolute;left:0;width:1200px;overflow:hidden}
.abs{position:absolute}
.center{left:0;width:1200px;text-align:center}
.section-title{font-size:36px;letter-spacing:6px;font-weight:400;top:70px}

/* hero */
.hero{top:0;height:474px;background:linear-gradient(180deg,var(--hero-a),var(--hero-b))}
.hero-photo{position:absolute;inset:0;background:radial-gradient(ellipse at 60% 30%,#6a4a3a 0%,#2a1e20 55%,#120e14 100%)}
.hero-shade{position:absolute;inset:0;background:rgba(0,0,0,.35)}
.nav{position:absolute;top:0;left:0;width:1200px;height:90px;background:rgba(20,20,20,.8)}
.brand{position:absolute;left:100px;top:30px;display:flex;align-items:center;gap:10px;font-size:15px;font-weight:600;letter-spacing:1px;color:var(--white)}
.brand-dot{width:22px;height:22px;border-radius:50%;background:var(--red)}
.nav-links{position:absolute;top:40px;left:450px;display:flex;gap:44px;font-size:13px;list-style:none}
.nav-links li{color:#cfcfcf}
.nav-links .active{color:var(--white);font-weight:700}
.hero-title{top:150px;font-family:"Playball",cursive;font-size:96px;color:var(--white);letter-spacing:6px}
.hero-title .initial{color:var(--red)}
.hero-sub{top:275px;font-size:30px;letter-spacing:6px}
.hero-text{top:360px;font-size:15px;line-height:22px}

/* welcome */
.welcome{top:474px;height:315px;background:var(--welcome)}
.welcome .section-title{top:52px}
.welcome-text{top:125px;font-size:17px;line-height:26px;color:#2a2a2a;letter-spacing:.4px}
.welcome-note{top:200px;font-size:12px;line-height:16px;color:var(--faint)}

/* about */
.about{top:789px;height:435px;background:var(--about)}
.about .section-title{top:48px}
.about-text{top:104px;font-size:17px;line-height:26px;letter-spacing:.4px}
.stat{position:absolute;top:190px;width:300px;text-align:center}
.stat-num{font-family:"Playfair Display",serif;font-style:italic;font-weight:700;font-size:30px;letter-spacing:4px;color:#e6e6e6}
.stat-title{font-size:15px;margin-top:14px}
.stat-text{font-size:13px;line-height:17px;margin-top:20px;color:#d9d9d9}
.divider{position:absolute;top:200px;width:1px;height:180px;background:#7c8e7d}

/* testimonial */
.testimonial{top:1224px;height:459px;background:var(--quote-bg);color:var(--ink)}
.quote-mark{top:20px;font-family:"Playfair Display",serif;font-weight:700;font-size:110px;color:var(--red);line-height:1;height:70px}
.quote-text{top:108px;left:220px;width:760px;text-align:center;font-weight:700;font-size:18px;line-height:28px;letter-spacing:1px;color:#2c3a2c}
.avatar{position:absolute;top:208px;left:525px;width:150px;height:150px;border-radius:50%;background:radial-gradient(circle at 45% 40%,var(--photo-warm),var(--photo-dark));border:2px solid #cfcfcf}
.quote-name{top:392px;font-size:13px}

/* events */
.events{top:1683px;height:684px;background:var(--red)}
.events .section-title{top:50px}
.event{position:absolute;top:150px;width:300px;text-align:center}
.event-photo{width:200px;height:200px;margin:0 auto;border-radius:50%;border:5px solid var(--white);background:radial-gradient(circle at 50% 45%,#b58a6a,#3a2a24)}
.event-photo.dish{background:radial-gradient(circle at 50% 50%,#f1e6d2,#b9a58a)}
.event-title{font-weight:700;font-size:16px;margin-top:55px}
.event-text{font-size:13px;line-height:16px;margin-top:22px;color:#f4d6d6}
.btn{position:absolute;display:flex;align-items:center;justify-content:center;background:var(--white);color:var(--ink);border-radius:10px;box-shadow:0 3px 5px rgba(0,0,0,.3)}
.events .btn{top:555px;left:468px;width:264px;height:60px;font-size:20px;letter-spacing:1px}

/* chefs */
.chefs{top:2367px;height:627px;background:var(--chefs)}
.chefs .section-title{top:48px}
.chef{position:absolute;top:138px;width:213px}
.chef-photo{width:213px;height:255px;border:2px solid #8a8a8a;background:linear-gradient(180deg,#9c7a5e 0%,#3d3a44 60%,#24262d 100%)}
.chef-name{height:69px;margin-top:18px;display:flex;align-items:center;justify-content:center;font-weight:700;font-size:16px;border:1px solid #999}
.chef-name.green{background:var(--chef-green);color:var(--white)}
.chef-name.light{background:var(--white);color:var(--red)}
.chef-name.red{background:var(--deep-red);color:#2a0a0a}
.socials{display:flex;gap:42px;justify-content:center;margin-top:28px}
.social{width:48px;height:48px;border-radius:8px;background:linear-gradient(180deg,#a9a9a9,#6f6f6f);border:1px solid #444}

/* menu */
.menu{top:2994px;height:810px;background:linear-gradient(180deg,var(--menu-b) 0%,var(--menu-a) 45%,#5c6b3c 70%,#1e2218 100%)}
.menu-photo{position:absolute;inset:0;background:radial-gradient(ellipse at 52% 48%,rgba(120,150,70,.6),rgba(20,22,26,.4) 70%)}
.menu-shade{position:absolute;inset:0;background:rgba(0,0,0,.25)}
.menu .section-title{top:42px}
.price{top:160px;font-size:56px;letter-spacing:5px}
.dish-name{top:255px;font-weight:700;font-size:30px}
.dish-text{top:306px;left:220px;width:760px;text-align:center;font-weight:700;font-size:18px;line-height:24px;letter-spacing:1px}
.arrow{position:absolute;top:150px}
.pager{position:absolute;top:738px;left:505px;display:flex;gap:18px}
.pager span{width:22px;height:22px;border-radius:50%;background:#6a6a6a}
.pager .current{background:#2a50d8}

/* contacts */
.contacts{top:3804px;height:615px;background:var(--contacts)}
.contacts .section-title{top:50px}
.field{position:absolute;left:126px;width:402px;height:54px;background:var(--field);border:1px solid #777;font-size:12px;letter-spacing:1px;color:#d6d6d6;padding:12px 14px}
.field.message{height:120px}
.contacts .btn{top:492px;left:129px;width:141px;height:60px;font-size:20px;border-radius:8px}
.address{position:absolute;left:660px;top:150px;font-size:24px;line-height:30px;letter-spacing:3px}
.phone{position:absolute;left:660px;top:226px;display:flex;gap:26px}
.phone-numbers{font-size:24px;line-height:30px;letter-spacing:3px}
.contact-note{position:absolute;left:555px;top:360px;width:600px;text-align:center;font-size:13px;line-height:17px;color:#e8eee9}

/* footer */
.footer{top:4419px;height:92px;background:var(--footer)}
.footer p{top:35px;font-size:15px}
</style>
</head>
<body>

<header class="hero">
  <div class="hero-photo" role="img" aria-label="Photo of the restaurant dining room with bar and chandelier"></div>
  <div class="hero-shade"></div>
  <nav class="nav">
    <div class="brand"><span class="brand-dot"></span>TEATRO LUNAVERDE</div>
    <ul class="nav-links">
      <li class="active">HOME</li><li>ABOUT</li><li>EVENTS</li><li>CHEFS</li><li>MENU</li><li>CONTACTS</li>
    </ul>
  </nav>
  <h1 class="abs center hero-title"><span class="initial">R</span>estaurant</h1>
  <p class="abs center hero-sub">ITALIAN &nbsp;CUISINE</p>
  <p class="abs center hero-text">Ut enim ad minim veniam, quis nostrud exercitation ullamco laboris nisi ut aliquip ex ea.<br>Duis aute irure dolor in reprehenderit in voluptate.</p>
</header>

<section class="welcome">
  <h2 class="abs center section-title">WELCOME!</h2>
  <p class="abs center welcome-text">Ut enim ad minim veniam, quis nostrud exercitation ullamco laboris nisi ut aliquip ex ea.<br>Duis aute irure dolor in reprehenderit in voluptate &nbsp;velit esse cillum dolore.</p>
  <p class="abs center welcome-note">Ut enim ad minim veniam quis nostrud exercitation ullamco laboris nisi ut aliquip ex ea.<br>Duis aute irure dolor in reprehenderit in voluptate velit esse cillum dolore.<br>Fugiat nulla pariatur.</p>
</section>

<section class="about">
  <h2 class="abs center section-title">ABOUT</h2>
  <p class="abs center about-text">Ut enim ad minim veniam, quis nostrud exercitation ullamco laboris nisi ut aliquip ex ea.<br>Duis aute irure dolor in reprehenderit in voluptate &nbsp;velit esse cillum dolore.</p>
  <div class="stat" style="left:141px"><div class="stat-num">1258</div><div class="stat-title">Ut enim ad minim veniam</div><div class="stat-text">Ut enim ad minim veniam<br>quis nostrud exercitation<br>ullamco nisi ut aliquip ex ea.<br>Duis aute irure dolor</div></div>
  <div class="divider" style="left:441px"></div>
  <div class="stat" style="left:450px"><div class="stat-num">758</div><div class="stat-title">Ut enim ad minim veniam</div><div class="stat-text">Ut enim ad minim veniam<br>quis nostrud exercitation<br>ullamco nisi ut aliquip ex ea.<br>Duis aute irure dolor</div></div>
  <div class="divider" style="left:759px"></div>
  <div class="stat" style="left:760px"><div class="stat-num">12758</div><div class="stat-title">Ut enim ad minim veniam</div><div class="stat-text">Ut enim ad minim veniam<br>quis nostrud exercitation<br>ullamco nisi ut aliquip ex ea.<br>Duis aute irure dolor</div></div>
</section>

<section class="testimonial">
  <div class="abs center quote-mark">&ldquo;</div>
  <p class="abs quote-text">Ut enim ad minim veniam, quis nostrud exercitation ullamco laboris nisi<br>ut aliquip ex ea. Duis aute irure dolor in reprehenderit in voluptate<br>velit esse lum dolore.</p>
  <div class="avatar" role="img" aria-label="Portrait of a guest holding a glass of wine"></div>
  <p class="abs center quote-name">Ut enim ad minim veniam</p>
</section>

<section class="events">
  <h2 class="abs center section-title">EVENTS</h2>
  <div class="event" style="left:99px"><div class="event-photo" role="img" aria-label="Portrait of the restaurant owner"></div><div class="event-title">Ut enim ad minim</div><div class="event-text">Ut enim ad minim veniam<br>quis nostrud exercitation ullamco<br>laboris nisi ut aliquip ex ea.<br>Duis aute irure dolor</div></div>
  <div class="event" style="left:450px"><div class="event-photo" role="img" aria-label="Photo of two hosts at an evening event"></div><div class="event-title">Ut enim ad minim</div><div class="event-text">Ut enim ad minim veniam<br>quis nostrud exercitation ullamco<br>laboris nisi ut aliquip ex ea.<br>Duis aute irure dolor</div></div>
  <div class="event" style="left:816px"><div class="event-photo dish" role="img" aria-label="Photo of a plated Italian dish"></div><div class="event-title">Ut enim ad minim</div><div class="event-text">Ut enim ad minim veniam<br>quis nostrud exercitation ullamco<br>laboris nisi ut aliquip ex ea.<br>Duis aute irure dolor</div></div>
  <div class="btn">READ MORE</div>
</section>

<section class="chefs">
  <h2 class="abs center section-title">CHEFS</h2>
  <div class="chef" style="left:159px"><div class="chef-photo" role="img" aria-label="Photo of a chef presenting a dish"></div><div class="chef-name green">Ut enim ad minim</div><div class="socials"><span class="social"></span><span class="social"></span></div></div>
  <div class="chef" style="left:492px"><div class="chef-photo" role="img" aria-label="Photo of a chef presenting a dish"></div><div class="chef-name light">Ut enim ad minim</div><div class="socials"><span class="social"></span><span class="social"></span></div></div>
  <div class="chef" style="left:825px"><div class="chef-photo" role="img" aria-label="Photo of a chef presenting a dish"></div><div class="chef-name red">Ut enim ad minim</div><div class="socials"><span class="social"></span><span class="social"></span></div></div>
</section>

<section class="menu">
  <div class="menu-photo" role="img" aria-label="Photo of a fresh mixed salad on a white plate"></div>
  <div class="menu-shade"></div>
  <h2 class="abs center section-title">MENU</h2>
  <svg class="arrow" style="left:48px" width="64" height="40" viewBox="0 0 64 40"><path d="M60 20H8M22 6L6 20l16 14" fill="none" stroke="#b9c3d6" stroke-width="6"/></svg>
  <svg class="arrow" style="left:1088px" width="64" height="40" viewBox="0 0 64 40"><path d="M4 20h52M42 6l16 14-16 14" fill="none" stroke="#b9c3d6" stroke-width="6"/></svg>
  <p class="abs center price">$25.89</p>
  <h3 class="abs center dish-name">Ut enim ad minim veniam</h3>
  <p class="abs dish-text">Ut enim ad minim veniam, quis nostrud exercitation ullamco laboris nisi<br>ut aliquip ex ea. Duis aute irure dolor in reprehenderit in voluptate<br>velit esse lum dolore.</p>
  <div class="pager"><span class="current"></span><span></span><span></span><span></span></div>
</section>

<section class="contacts">
  <h2 class="abs center section-title">CONTACTS</h2>
  <div class="field" style="top:150px">Name:</div>
  <div class="field" style="top:213px">E-mail:</div>
  <div class="field" style="top:276px">Phone:</div>
  <div class="field message" style="top:339px">Message:</div>
  <div class="btn">SEND</div>
  <p class="address">Address: 00 Voorbeeldstraat,<br>Amsterdam 0000 XX.</p>
  <div class="phone">
    <svg width="38" height="38" viewBox="0 0 24 24"><path fill="#ffffff" d="M6.6 10.8a15 15 0 0 0 6.6 6.6l2.2-2.2c.3-.3.7-.4 1-.2 1.1.4 2.3.6 3.6.6.6 0 1 .4 1 1V20c0 .6-.4 1-1 1A17 17 0 0 1 3 4c0-.6.4-1 1-1h3.5c.6 0 1 .4 1 1 0 1.3.2 2.5.6 3.6.1.3 0 .7-.2 1z"/></svg>
    <div class="phone-numbers">800 555-0142<br>800 555-0142</div>
  </div>
  <p class="contact-note">Ut enim ad minim veniam, quis nostrud exercitation ullamco<br>laboris nisi ut aliquip ex ea. Duis aute irure dolor in reprehenderit in voluptate<br>velit esse cillum dolore.</p>
</section>

<footer class="footer">
  <p class="abs center">Restaurant@2018.</p>
</footer>

</body>
</html>
```